5 Years of Lunemar Research

This is a book cover for a new research book that will include 5 years of clinical case studies showing patients' dramatic health improvements from mental illness, chronic inflammatory conditions, cancer, and injury, all following concentrated chiropractic care at Lunemar Health Institute. Our logo needs to be incorporated into the design subtly.
Please USE our website as reference to our facilty and design preferences: https://lunemarhealth-example.com/
Please USE information from the Internationally Published Research tab, which shows all of the cases that will be included in this book, plus a case on reversing cerebral palsy that will be published in a few weeks.

This needs to be a design made for a 8.5x11 sized book.

Target Market(s)

People with chronic disease or health problem

Industry/Entity Type

Healthcare

Font styles to use
Serif
Other font styles liked:
• Avenir, Graphic, Optimum, Century Gothic

Colors
00AB8E
00BBA5
67D7C9
C6EFE9
E9F9F6
FFC000
F8CF3A
FAE287
FDF2CF
FEFAEE

Requirements
Must have
• It must be profession. Our colors are dark green / gold / white.
Nice to have
• I would like to see something that is eye-catching and would encourage a person to buy and read this book. Including spine/brain/chiropractic images is optimal.

```html
<!DOCTYPE html>
<html lang="en">
<head>
<meta charset="utf-8">
<title>5 Years of Lunemar Research</title>
<link rel="stylesheet" href="https://fonts.googleapis.com/css2?family=Noto+Serif:ital,wght@0,600;0,700;0,800;1,400&display=swap">
<style>
  :root {
    --backdrop: #000000;
    --paper: #ffffff;
    --leaf: #35964a;
    --gold: #fcc217;
    --gold-glow: #fff4a8;
    --outline: #2f6a2c;
    --ink: #111111;
    --meadow-light: #eef6dc;
    --meadow-mid: #c3e0a0;
    --meadow-deep: #8fc45e;
  }
  html, body {
    margin: 0;
    padding: 0;
    width: 1200px;
    height: 1200px;
    overflow: hidden;
    background: var(--backdrop);
  }
  .book-cover {
    position: absolute;
    left: 240px;
    top: 60px;
    width: 720px;
    height: 1080px;
    background: var(--paper);
    overflow: hidden;
  }
  .cover-art {
    position: absolute;
    inset: 0;
    width: 720px;
    height: 1080px;
  }
  .title-text {
    font-family: "Noto Serif", Georgia, serif;
    font-weight: 700;
  }
  .title-green { fill: var(--leaf); }
  .title-gold {
    fill: var(--gold);
    stroke: var(--outline);
    stroke-width: 1.6;
    paint-order: stroke fill;
  }
  .numeral {
    font-family: "Noto Serif", Georgia, serif;
    font-weight: 600;
    fill: var(--gold);
    stroke: var(--outline);
    stroke-width: 1.8;
    filter: drop-shadow(0 0 8px var(--gold-glow)) drop-shadow(0 0 4px var(--gold-glow));
  }
  .subtitle {
    font-family: "Noto Serif", Georgia, serif;
    font-style: italic;
    font-weight: 400;
    font-size: 37px;
    fill: var(--ink);
    letter-spacing: 1px;
  }
  .author-name {
    font-family: "Noto Serif", Georgia, serif;
    font-weight: 700;
    font-size: 56px;
    fill: var(--paper);
    stroke: #4d6b3a;
    stroke-width: 1.2;
    letter-spacing: 3px;
  }
</style>
</head>
<body>
  <div class="book-cover">
    <svg class="cover-art" viewBox="0 0 720 1080" xmlns="http://www.w3.org/2000/svg">
      <defs>
        <linearGradient id="meadowFade" x1="0" y1="0" x2="0" y2="1">
          <stop offset="0" stop-color="#ffffff" stop-opacity="0"/>
          <stop offset="0.3" stop-color="#f7f9e6"/>
          <stop offset="0.6" stop-color="#d4e8b2"/>
          <stop offset="1" stop-color="#9ccb6c"/>
        </linearGradient>
      </defs>

      <rect class="meadow-backdrop" role="img" aria-label="Soft green honeycomb texture fading upward into white"
            x="0" y="370" width="720" height="710" fill="url(#meadowFade)"/>

      <text class="numeral" x="44" y="288" font-size="332" textLength="164" lengthAdjust="spacingAndGlyphs">5</text>

      <text class="title-text title-green" x="238" y="143" font-size="128" textLength="438" lengthAdjust="spacingAndGlyphs">YEARS</text>
      <text class="title-text title-gold" x="416" y="196" font-size="62" textLength="80" lengthAdjust="spacingAndGlyphs">OF</text>
      <text class="title-text title-green" x="238" y="287" font-size="111" textLength="438" lengthAdjust="spacingAndGlyphs">LUNEMAR</text>
      <text class="title-text title-gold" x="44" y="387" font-size="114" textLength="632" lengthAdjust="spacingAndGlyphs">RESEARCH</text>

      <text class="subtitle" x="360" y="456" text-anchor="middle">Transforming Health Through</text>
      <text class="subtitle" x="360" y="506" text-anchor="middle">Chiropractic Care</text>

      <text class="author-name" x="360" y="1030" text-anchor="middle">AUTHOR NAME</text>
    </svg>
  </div>
</body>
</html>
```